Torvel, Inc. new buisness cards - brand guide included

We need new business cards. SLEAK SIMPLE FINANCE. They must include a place for NAME, TITLE, CELL, OFFICE PHONE, EMAIL. they also must include our services across the bottom. AIR, OCEAN, FTL, LTL, EXPRESS. for reference this will be being handed to some of the most prestigious shipping companies in a america.

Target Market(s)

Finance and corporate

Contact Information for Business Card

We need new business cards. SLEAK SIMPLE FINANCE. They must include a place for NAME, TITLE, CELL, OFFICE PHONE, EMAIL. they also must include our services across the bottom. AIR, OCEAN, FTL, LTL, EXPRESS.

Requirements
Must have
• We need new business cards. SLEAK SIMPLE FINANCE. They must include a place for NAME, TITLE, CELL, OFFICE PHONE, EMAIL. they also must include our services across the bottom. AIR, OCEAN, FTL, LTL, EXPRESS.
Nice to have
• USE THE COLORS AND LOGO IN THE BRAND GUIDE :)

```html
<!DOCTYPE html>
<html lang="en">
<head>
<meta charset="utf-8">
<title>Torvel, Inc. Business Card</title>
<link rel="stylesheet" href="https://fonts.googleapis.com/css2?family=Montserrat:wght@400;500;600&display=swap">
<style>
  :root {
    --stage: #3b3b3c;
    --card-white: #ffffff;
    --sand: #c5b595;
    --sand-deep: #b9a780;
    --ink: #1f1f1f;
    --cream: #f4f0ea;
  }
  html, body {
    margin: 0;
    width: 1200px;
    height: 1200px;
    overflow: hidden;
    background: var(--stage);
    font-family: "Montserrat", sans-serif;
  }
  .canvas {
    position: relative;
    width: 1200px;
    height: 1200px;
  }
  .card {
    position: absolute;
    left: 170px;
    width: 860px;
    height: 500px;
    border-radius: 36px;
    overflow: hidden;
    box-shadow: 0 14px 30px rgba(0,0,0,0.35);
  }
  .card--front { top: 70px; background: var(--card-white); }
  .card--back { top: 630px; background: var(--sand); }

  .card__swoosh {
    position: absolute;
    inset: 0;
    width: 100%;
    height: 100%;
  }

  .contact {
    position: absolute;
    left: 74px;
    top: 196px;
    color: var(--ink);
  }
  .contact__name {
    margin: 0;
    font-size: 34px;
    font-weight: 600;
    letter-spacing: 0.5px;
    color: var(--sand-deep);
    line-height: 1;
  }
  .contact__title {
    margin: 4px 0 20px;
    font-size: 21px;
    font-weight: 500;
    letter-spacing: 0.5px;
  }
  .contact__list {
    list-style: none;
    margin: 0;
    padding: 0;
  }
  .contact__item {
    display: flex;
    align-items: center;
    gap: 14px;
    font-size: 22px;
    font-weight: 400;
    line-height: 1;
    margin-bottom: 12px;
  }
  .contact__icon {
    width: 24px;
    height: 24px;
    flex: none;
  }

  .brand {
    position: absolute;
    right: 80px;
    top: 64px;
    text-align: center;
  }
  .brand__name {
    margin: 0;
    font-size: 62px;
    font-weight: 500;
    letter-spacing: 6px;
    color: var(--sand-deep);
    line-height: 1;
  }
  .brand__services {
    margin: 22px 0 0;
    font-size: 16px;
    font-weight: 500;
    letter-spacing: 1px;
    color: var(--ink);
  }
  .brand__dot { color: var(--sand-deep); padding: 0 5px; }

  .back-brand {
    position: absolute;
    inset: 0;
    display: flex;
    align-items: center;
    justify-content: center;
  }
  .back-brand__name {
    margin: 0;
    font-size: 96px;
    font-weight: 500;
    letter-spacing: 10px;
    color: var(--cream);
  }
</style>
</head>
<body>
<main class="canvas">

  <section class="card card--front" aria-label="Business card front">
    <svg class="card__swoosh" viewBox="0 0 860 500" preserveAspectRatio="none" aria-hidden="true">
      <path d="M0,480 C200,452 390,444 550,378 C690,320 795,292 860,222 L860,500 L0,500 Z" fill="var(--sand)"/>
      <path d="M0,468 C200,440 390,432 550,366 C690,308 795,280 860,210" fill="none" stroke="var(--card-white)" stroke-width="8"/>
      <path d="M0,458 C200,430 390,422 550,356 C690,298 790,268 845,212" fill="none" stroke="var(--sand)" stroke-width="4"/>
    </svg>

    <div class="contact">
      <h1 class="contact__name">FULL NAME</h1>
      <p class="contact__title">TITLE</p>
      <ul class="contact__list">
        <li class="contact__item">
          <svg class="contact__icon" viewBox="0 0 24 24" aria-hidden="true"><rect x="6" y="1.5" width="12" height="21" rx="2" fill="none" stroke="var(--sand-deep)" stroke-width="1.6"/><line x1="10" y1="19" x2="14" y2="19" stroke="var(--sand-deep)" stroke-width="1.6"/></svg>
          (000) 000 0000
        </li>
        <li class="contact__item">
          <svg class="contact__icon" viewBox="0 0 24 24" aria-hidden="true"><path d="M6.6 10.8a15 15 0 0 0 6.6 6.6l2.2-2.2a1 1 0 0 1 1-.25 11.4 11.4 0 0 0 3.6.57 1 1 0 0 1 1 1V20a1 1 0 0 1-1 1A17 17 0 0 1 3 4a1 1 0 0 1 1-1h3.5a1 1 0 0 1 1 1c0 1.25.2 2.45.57 3.6a1 1 0 0 1-.25 1z" fill="var(--sand-deep)"/></svg>
          (000) 000 0000
        </li>
        <li class="contact__item">
          <svg class="contact__icon" viewBox="0 0 24 24" aria-hidden="true"><rect x="2" y="5" width="20" height="14" fill="var(--sand-deep)"/><path d="M2 5l10 8 10-8M2 19l7-7M22 19l-7-7" fill="none" stroke="var(--card-white)" stroke-width="1.4"/></svg>
          email@company.com
        </li>
      </ul>
    </div>

    <div class="brand">
      <p class="brand__name">TORVEL</p>
      <p class="brand__services">AIR<span class="brand__dot">•</span>OCEAN<span class="brand__dot">•</span>FTL<span class="brand__dot">•</span>LTL<span class="brand__dot">•</span>EXPRESS</p>
    </div>
  </section>

  <section class="card card--back" aria-label="Business card back">
    <div class="back-brand">
      <p class="back-brand__name">TORVEL</p>
    </div>
  </section>

</main>
</body>
</html>
```